Corvale Fitouts Web

We just need an update/re-design of our existing web site that would include our new company logo and some new photo's. Our current web site can be viewed at www.corvalefitouts.com.au. We would require something very similar to what we have at the moment in terms of content it should all be the same.
The web site would basically act more as a portfolio than one that would generate more business.
We are after a very modern and simple design and maybe something where we can upload our own project photo's and project descriptions as we complete them.

```html
<!DOCTYPE html>
<html lang="en">
<head>
<meta charset="utf-8">
<title>Corvale Fitouts</title>
<link rel="stylesheet" href="https://fonts.googleapis.com/css2?family=Arimo:wght@400;700&family=PT+Sans+Narrow:wght@400;700&family=Open+Sans:wght@300&display=swap">
<style>
:root{
  --ink:#222;
  --heading:#4a4a4a;
  --body:#555;
  --page:#f4f4f4;
  --white:#fff;
  --dark:#1e1c1c;
  --footer:#121212;
  --rule:#8a8a8a;
  --footer-rule:#3a3a3a;
  --hero-sky:#8fb4d8;
  --hero-glass:#2c4a70;
  --hero-clad:#5a3a30;
}
*{margin:0;padding:0;box-sizing:border-box}
html,body{width:726px;height:1200px;overflow:hidden}
body{position:relative;background:var(--page);font-family:"Arimo",Arial,sans-serif;color:var(--body)}
.abs{position:absolute}

/* header */
.site-header{position:absolute;left:0;top:0;width:726px;height:91px;background:var(--white);border-bottom:1px solid #ddd}
.brand{position:absolute;left:72px;top:24px;font-family:"Open Sans",sans-serif;font-weight:300;font-size:31px;color:#444;letter-spacing:-0.5px}
.main-nav{position:absolute;left:440px;top:40px;display:flex;align-items:center;font-size:8px;color:var(--ink)}
.main-nav a{color:var(--ink);text-decoration:none}
.main-nav .current{background:var(--dark);color:var(--white);border-radius:3px;padding:0 11px;height:23px;line-height:23px;font-weight:700;margin-right:8px}
.main-nav .sep{color:#aaa;margin:0 4px}

/* hero */
.hero{position:absolute;left:0;top:91px;width:726px;height:289px;
  background:linear-gradient(160deg,var(--hero-sky) 0%,#c8d8e8 25%,var(--hero-glass) 45%,#1f3350 65%,var(--hero-clad) 85%,#3a2a26 100%)}
.slider-control{position:absolute;left:326px;top:344px;width:68px;height:36px}

/* content */
.title{position:absolute;font-family:"PT Sans Narrow",sans-serif;font-weight:700;color:var(--heading);text-align:center}
.welcome{left:0;width:716px;top:414px;font-size:19px}
.intro{position:absolute;left:0;width:716px;top:448px;font-size:8px;text-align:center;color:var(--body)}
.rule-title{position:absolute;left:70px;width:575px;display:flex;align-items:center;font-family:"PT Sans Narrow",sans-serif;font-weight:700;color:var(--heading)}
.rule-title::before,.rule-title::after{content:"";flex:1;height:1px;background:var(--rule)}
.rule-title span{padding:0 6px}
.projects-title{top:482px;font-size:18px}
.services-title{top:790px;font-size:15px}
.carousel-arrows{position:absolute;left:611px;top:504px;display:flex;gap:3px}

.project{position:absolute;width:170px;text-align:center}
.project .photo{width:170px;height:108px;background:var(--white);padding:4px;box-shadow:0 1px 4px rgba(0,0,0,.35)}
.project .photo div{width:100%;height:100%}
.project h3{font-family:"PT Sans Narrow",sans-serif;font-weight:700;font-size:15px;color:var(--heading);margin-top:14px}
.project p{font-size:8px;line-height:9.5px;text-align:justify;color:#444;margin:2px 4px 0}
.btn-more{display:inline-block;background:var(--dark);color:var(--white);font-size:8px;height:25px;line-height:25px;width:59px;border-radius:2px;margin-top:15px}

.service{position:absolute;display:flex;align-items:center;font-size:8.5px;color:var(--body)}
.service svg{margin-right:8px}
.about{position:absolute;left:72px;top:920px;width:572px;font-size:8.5px;line-height:11px;color:var(--body)}
.about p+p{margin-top:11px}

/* footer */
.site-footer{position:absolute;left:0;top:1014px;width:726px;height:186px;background:var(--footer);color:var(--white)}
.f-col{position:absolute;top:16px}
.f-col h4{font-family:"PT Sans Narrow",sans-serif;font-weight:700;font-size:12px;padding-bottom:6px;border-bottom:1px solid var(--footer-rule)}
.f-nav{left:72px;width:108px}
.f-nav li{list-style:none;font-size:7px;margin-top:12px}
.f-contact{left:227px;width:168px}
.f-contact .addr{font-size:7px;margin-top:8px}
.f-contact .line{display:flex;align-items:center;font-size:7px;margin-top:9px}
.f-contact .line svg{margin-right:10px}
.f-follow{left:437px;width:140px}
.socials{display:flex;gap:5px;margin-top:8px}
.socials span{width:28px;height:28px;border-radius:50%;background:var(--white)}
.f-follow h4.news{margin-top:10px;border:none}
.news-input{width:153px;height:14px;background:var(--white);border-radius:2px;margin-top:2px}
.join{position:absolute;left:547px;top:1138px;width:43px;height:19px;background:var(--white);color:var(--ink);font-size:8px;text-align:center;line-height:19px}
.vsep{position:absolute;top:1030px;width:1px;height:108px;background:var(--footer-rule)}
.copyright{position:absolute;left:66px;top:1139px;font-size:6.5px;color:var(--white)}
</style>
</head>
<body>

<header class="site-header">
  <div class="brand">Corvale Fitouts</div>
  <nav class="main-nav">
    <a class="current" href="#">Home</a>
    <a href="#">Recent Projects</a><span class="sep">:</span>
    <a href="#">Our Services</a><span class="sep">:</span>
    <a href="#">Our Contact</a>
  </nav>
</header>

<div class="hero" role="img" aria-label="Photograph of a modern commercial building with a glass curtain wall and timber cladding under a blue sky"></div>
<svg class="slider-control" viewBox="0 0 68 36">
  <path d="M0 36 A34 34 0 0 1 68 36 Z" fill="#fff"/>
  <path d="M24 18 l-5 6 l5 6" fill="none" stroke="#999" stroke-width="2"/>
  <line x1="34" y1="17" x2="34" y2="31" stroke="#ccc"/>
  <path d="M44 18 l5 6 l-5 6" fill="none" stroke="#999" stroke-width="2"/>
</svg>

<h1 class="title welcome">Welcome to Corvale Fitouts</h1>
<p class="intro">Corvale Fitouts Pty Ltd was established in 2005 and has been operating in the Sydney area, but has completed numerous projects outside of Sydney.</p>

<h2 class="rule-title projects-title"><span>Recent Projects</span></h2>
<div class="carousel-arrows">
  <svg width="15" height="16" viewBox="0 0 15 16"><rect width="15" height="16" rx="3" fill="#888"/><path d="M9 4 l-4 4 l4 4" fill="none" stroke="#fff" stroke-width="2"/></svg>
  <svg width="15" height="16" viewBox="0 0 15 16"><rect width="15" height="16" rx="3" fill="#888"/><path d="M6 4 l4 4 l-4 4" fill="none" stroke="#fff" stroke-width="2"/></svg>
</div>

<article class="project" style="left:82px;top:537px">
  <div class="photo"><div role="img" aria-label="Project photo of an office lobby with timber ceiling and stairs" style="background:linear-gradient(180deg,#3a3a3a,#9a8a78 45%,#c9c5bc)"></div></div>
  <h3>Lorem Ipsum</h3>
  <p>Loremipsum dolor sit amet, dui a, massarutrum-maurisarcuaugueamet ac, in maurisnisinatoque, odiovivamusquisque mi ac portanonummy, proin-arcuurabitur.</p>
  <span class="btn-more">Read more...</span>
</article>
<article class="project" style="left:281px;top:537px">
  <div class="photo"><div role="img" aria-label="Project photo of a multi storey office building exterior" style="background:linear-gradient(180deg,#b8c0c8,#6a6a6e 50%,#4a4a4e)"></div></div>
  <h3>Lorem Ipsum</h3>
  <p>Loremipsum dolor sit amet, dui a, massarutrum-maurisarcuaugueamet ac, in maurisnisinatoque, odiovivamusquisque mi ac portanonummy, proin-arcuurabitur.</p>
  <span class="btn-more">Read more...</span>
</article>
<article class="project" style="left:483px;top:535px">
  <div class="photo"><div role="img" aria-label="Project photo of a bulkhead ceiling with warm cove lighting" style="background:linear-gradient(180deg,#3a2c1c,#c9a060 50%,#5a4632)"></div></div>
  <h3>Lorem Ipsum</h3>
  <p>Loremipsum dolor sit amet, dui a, massarutrum-maurisarcuaugueamet ac, in maurisnisinatoque, odiovivamusquisque mi ac portanonummy, proinar-cuurabitur.</p>
  <span class="btn-more">Read more...</span>
</article>

<h2 class="rule-title services-title"><span>We specialise in the internal fit outs to</span></h2>

<div class="service" style="left:70px;top:825px">
  <svg width="30" height="28" viewBox="0 0 30 28"><path d="M0 28 V14 l7-5 v5 l7-5 v5 l7-5 V4 h3 v-3 h3 V28 Z" fill="#222"/></svg>Industrial Offices
</div>
<div class="service" style="left:196px;top:822px">
  <svg width="18" height="34" viewBox="0 0 18 34"><path d="M3 34 V6 h4 V0 h4 v6 h4 v28 Z" fill="#222"/><g fill="#fff"><rect x="5" y="9" width="2" height="2"/><rect x="11" y="9" width="2" height="2"/><rect x="5" y="15" width="2" height="2"/><rect x="11" y="15" width="2" height="2"/><rect x="5" y="21" width="2" height="2"/><rect x="11" y="21" width="2" height="2"/><rect x="5" y="27" width="2" height="2"/><rect x="11" y="27" width="2" height="2"/></g></svg>Multi Storey Offices
</div>
<div class="service" style="left:342px;top:829px">
  <svg width="30" height="18" viewBox="0 0 30 18"><rect y="2" width="30" height="16" fill="#222"/><g fill="#fff"><rect x="3" y="6" width="3" height="3"/><rect x="9" y="6" width="3" height="3"/><rect x="15" y="6" width="3" height="3"/><rect x="21" y="6" width="3" height="3"/><rect x="3" y="12" width="3" height="3"/><rect x="9" y="12" width="3" height="3"/><rect x="15" y="12" width="3" height="3"/><rect x="21" y="12" width="3" height="3"/></g></svg>External Facades
</div>
<div class="service" style="left:508px;top:819px">
  <svg width="36" height="32" viewBox="0 0 36 32"><path d="M2 32 V8 h10 V0 h16 V32 Z" fill="#222"/><g fill="#fff"><rect x="15" y="4" width="3" height="3"/><rect x="22" y="4" width="3" height="3"/><rect x="15" y="11" width="3" height="3"/><rect x="22" y="11" width="3" height="3"/><rect x="15" y="18" width="3" height="3"/><rect x="22" y="18" width="3" height="3"/><rect x="5" y="12" width="3" height="3"/><rect x="5" y="19" width="3" height="3"/></g></svg><span style="margin-left:8px">Commercial Projects</span>
</div>
<div class="service" style="left:68px;top:877px">
  <svg width="28" height="14" viewBox="0 0 28 14"><path d="M0 14 V6 l7-6 l7 6 l7-5 l7 5 V14 Z" fill="#222"/><g fill="#fff"><rect x="4" y="8" width="3" height="3"/><rect x="10" y="8" width="2" height="3"/><rect x="18" y="8" width="3" height="3"/></g></svg>Residential Houses
</div>

<div class="about">
  <p>The key group of our operating staff have all been involved in the construction industry for well over 20 years. Our employees are skilled and trained and have the experience to deliver the best possible product, safely and on time.</p>
  <p>At Corvale Fitouts we pride ourselves on working together.</p>
</div>

<footer class="site-footer">
  <div class="f-col f-nav">
    <h4>Navigation</h4>
    <ul><li>Home</li><li>Recent Projects</li><li>Our Services</li><li>Contact Us</li></ul>
  </div>
  <div class="f-col f-contact">
    <h4>Contact Info</h4>
    <div class="addr">14/52 Harrowfield Road Wetherill Park</div>
    <div class="line"><svg width="10" height="12" viewBox="0 0 10 12"><path d="M3 0 l2 3 l-1.5 1.5 q1 3 3 4 L8 7 l2 2 l-2 3 Q1 11 0 2 Z" fill="#fff"/></svg>(02) 9000 4412</div>
    <div class="line"><svg width="12" height="12" viewBox="0 0 12 12"><rect x="3" y="0" width="6" height="4" fill="none" stroke="#fff"/><rect x="0" y="4" width="12" height="8" fill="#fff"/><rect x="2" y="6" width="8" height="2" fill="#121212"/></svg>(02) 9000 4418</div>
    <div class="line"><svg width="12" height="9" viewBox="0 0 12 9"><rect width="12" height="9" fill="#fff"/><path d="M0 0 l6 5 l6-5" fill="none" stroke="#121212"/></svg>info@corvalefitouts.com.au</div>
  </div>
  <div class="f-col f-follow">
    <h4>Follow Us</h4>
    <div class="socials"><span></span><span></span><span></span></div>
    <h4 class="news">Newsletter</h4>
    <div class="news-input"></div>
  </div>
</footer>
<div class="vsep" style="left:202px"></div>
<div class="vsep" style="left:418px"></div>
<div class="join">Join us</div>
<div class="copyright">© Copyright Corvale Fitouts Pty Ltd 2014</div>

</body>
</html>
```